Pebble Lantern Fine Chocolates
Handcrafted in Tucson, Arizona
tolquartdraws: would you like to try stationary to go with #29?? I like all the dripping chocolate :) Maybe also make the logo slightly bigger and remove the little icons in front of contact info?? Thanks!!
Oh, and I guess you would not have to text Tucson, Arizona since that is already in the Logo.
I am really am liking all these variations. I'm not sure I like the little icons in front of name, phone, email, web address, etc. I would like it to be clear and easy to read quickly, also artistic. Thanks for all your submissions!!

```html
<!DOCTYPE html>
<html lang="en">
<head>
<meta charset="utf-8">
<title>Pebble Lantern Fine Chocolates – Stationery</title>
<link href="https://fonts.googleapis.com/css2?family=Cormorant+Garamond:wght@600&family=Lato:wght@400&display=swap" rel="stylesheet">
<style>
  :root{
    --bg-dark:#6e1a1f;
    --bg-mid:#8c2a2f;
    --red:#a3131c;
    --red-deep:#7d0c12;
    --black:#1a1414;
    --paper:#ffffff;
    --paper-shade:#ececec;
    --brown:#5a3220;
    --ink:#6b6b6b;
    --faint:#ece6d8;
  }
  *{box-sizing:border-box;margin:0;padding:0}
  html,body{width:1200px;height:302px;overflow:hidden}
  body{
    position:relative;
    background:radial-gradient(ellipse at 45% 40%,var(--bg-mid),var(--bg-dark) 80%);
    font-family:'Lato',sans-serif;color:var(--ink);
  }
  .piece{position:absolute;background:var(--paper);box-shadow:0 2px 6px rgba(0,0,0,.35)}

  /* brand name: one colour, one weight, optional plain circle beside */
  .brand{
    position:absolute;display:flex;align-items:center;gap:3px;white-space:nowrap;
    font-family:'Cormorant Garamond',serif;font-weight:600;color:var(--brown);line-height:1;
  }
  .brand .dot{display:block;border-radius:50%;background:var(--red);flex:none}
  .brand.on-dark{color:var(--paper)}
  .brand.faint{color:var(--faint)}

  .main-brand{left:40px;top:44px;font-size:17px}
  .main-brand .dot{width:10px;height:10px}

  .card{width:82px;height:40px;top:130px;overflow:hidden}
  .card .band{position:absolute;left:0;top:0;bottom:0;width:5px;background:var(--red)}
  .card .brand{left:9px;top:4px;font-size:5px}
  .card .brand .dot{width:4px;height:4px}
  .card .details{position:absolute;left:9px;top:14px;font-size:3.4px;line-height:5px}
  .card.back{background:var(--red)}
  .card.back .brand{left:0;right:0;top:16px;justify-content:center;font-size:6px}
  .card-front-1{left:22px}
  .card-front-2{left:110px}
  .card-back{left:198px}

  .truffle-photo{position:absolute;left:100px;top:204px;width:86px;height:38px;
    background:linear-gradient(135deg,#c9a9a2,#5a2a22 55%,#2e1410);box-shadow:0 2px 6px rgba(0,0,0,.35)}

  .letterhead{top:18px;width:196px;height:265px;overflow:hidden}
  .letterhead .edge{position:absolute;left:0;top:0;bottom:0;width:12px;background:linear-gradient(90deg,var(--red-deep),var(--red))}
  .letterhead .brand.top{left:60px;top:16px;font-size:7px}
  .letterhead .brand.top .dot{width:5px;height:5px}
  .letterhead .brand.faint{left:12px;right:0;top:125px;justify-content:center;font-size:16px}
  .letterhead-one{left:283px}
  .letterhead-two{left:504px}
  .letterhead-one .brand.top{left:40px}
  .letterhead-one .contact{position:absolute;left:126px;top:8px;font-size:3.6px;line-height:5px}
  .letterhead-two .brand.top{left:12px;right:0;justify-content:center}
  .letterhead-two .footer{position:absolute;left:20px;right:10px;bottom:8px;font-size:3.6px;text-align:center;border-top:1px solid var(--red);padding-top:3px}

  .envelope{left:715px;width:210px;height:110px;overflow:hidden}
  .envelope .edge{position:absolute;left:0;top:0;bottom:0;width:10px;background:var(--red)}
  .envelope .brand{left:16px;top:10px;font-size:6px}
  .envelope .brand .dot{width:4px;height:4px}
  .envelope .return{position:absolute;left:16px;top:20px;font-size:3.6px;line-height:5px}
  .envelope .brand.faint{left:10px;right:0;top:50px;justify-content:center;font-size:14px}
  .envelope-top{top:42px}
  .envelope-bottom{top:174px}

  .dl{left:940px;width:236px;height:82px;overflow:hidden;background:var(--paper-shade)}
  .dl svg{position:absolute;inset:0}
  .dl .brand{left:0;right:0;top:12px;justify-content:center;font-size:6px}
  .dl-black{top:22px}
  .dl-red{top:104px}
  .dl-white{top:200px}
</style>
</head>
<body>
  <div class="brand main-brand"><span class="dot"></span>Pebble Lantern</div>

  <div class="piece card card-front-1"><span class="band"></span>
    <div class="brand"><span class="dot"></span>Pebble Lantern</div>
    <p class="details">Ana Ruiz · Head Chocolatier<br>520 555 0148<br>hello@pebblelantern.com</p></div>
  <div class="piece card card-front-2"><span class="band"></span>
    <div class="brand"><span class="dot"></span>Pebble Lantern</div>
    <p class="details">Ana Ruiz · Head Chocolatier<br>520 555 0148<br>hello@pebblelantern.com</p></div>
  <div class="piece card back card-back"><div class="brand on-dark">Pebble Lantern</div></div>

  <div class="truffle-photo" role="img" aria-label="Photo of chocolate truffles with dripping chocolate"></div>

  <div class="piece letterhead letterhead-one"><span class="edge"></span>
    <div class="brand top"><span class="dot"></span>Pebble Lantern</div>
    <p class="contact">12 Canyon Road<br>520 555 0148<br>pebblelantern.com</p>
    <div class="brand faint">Pebble Lantern</div></div>

  <div class="piece letterhead letterhead-two"><span class="edge"></span>
    <div class="brand top"><span class="dot"></span>Pebble Lantern</div>
    <div class="brand faint">Pebble Lantern</div>
    <p class="footer">12 Canyon Road · 520 555 0148 · pebblelantern.com</p></div>

  <div class="piece envelope envelope-top"><span class="edge"></span>
    <div class="brand"><span class="dot"></span>Pebble Lantern</div>
    <p class="return">12 Canyon Road<br>Tucson, Arizona</p>
    <div class="brand faint">Pebble Lantern</div></div>
  <div class="piece envelope envelope-bottom"><span class="edge"></span>
    <div class="brand"><span class="dot"></span>Pebble Lantern</div>
    <p class="return">12 Canyon Road<br>Tucson, Arizona</p>
    <div class="brand faint">Pebble Lantern</div></div>

  <div class="piece dl dl-black">
    <svg viewBox="0 0 236 82" width="236" height="82"><polygon points="0,0 236,0 236,10 118,46 0,10" fill="var(--black)"/></svg>
    <div class="brand on-dark">Pebble Lantern</div></div>
  <div class="piece dl dl-red">
    <svg viewBox="0 0 236 82" width="236" height="82"><polygon points="0,0 236,0 236,10 118,46 0,10" fill="var(--red)"/></svg>
    <div class="brand on-dark">Pebble Lantern</div></div>
  <div class="piece dl dl-white">
    <svg viewBox="0 0 236 82" width="236" height="82"><rect width="236" height="82" fill="var(--paper)"/><polyline points="0,4 118,44 236,4" fill="none" stroke="#cfcfcf" stroke-width="1"/></svg></div>
</body>
</html>
```